"Brightwall Sound Living Residences" need a busines Card Design got Builder

We need a business card design for a company based in Milford, Michigancalled Brightwall Sound Living Residences - has been recognized as a premier custom home builder. Distinguished by outstanding craftmanship and timeless beauty. Our custom home can be found in the most prestigious communities in Michigan. The homes are built with ICF (insulated concrete homes) which is green, allergy free, fire free, mold free and quitter. Our slogan "building one dream at a Time" and also we are ICF distributor for the state of Michigan

Target Market(s)

Anyone who is making over $100,000 a year and who wants to have totally custom built home. Ages from 29 up to 60 years old

Industry/Entity Type

Concrete

Contact Information for Business Card

we want to use - green, black, gray or blue colors - we want to look different with our business cards, because we built homes only with ICF, green, healthier and highly energy efficient homes.

Requirements
Must have
• I have logo that I attached and we have been using the logo (the only green home)
Nice to have
• should look quality business card,

Files

```html
<!DOCTYPE html>
<html lang="en">
<head>
<meta charset="utf-8">
<title>Brightwall Sound Living Residences – Business Card</title>
<link rel="stylesheet" href="https://fonts.googleapis.com/css2?family=Quicksand:wght@400;500;600&display=swap">
<style>
  :root{
    --bg:#2a2a2a;
    --green:#9bcb47;
    --white:#ffffff;
    --gray:#6b6b6b;
    --gray-light:#9a9a9a;
  }
  *{margin:0;padding:0;box-sizing:border-box}
  html,body{width:1200px;height:1000px;overflow:hidden;background:var(--bg)}
  body{font-family:"Quicksand",sans-serif;position:relative}
  .card{position:absolute;left:300px;width:600px;height:360px;border-radius:26px;overflow:hidden}
  .card-front{top:70px;background:var(--green);color:var(--white)}
  .card-back{top:560px;background:var(--white)}
  .wedges{position:absolute;inset:0;width:100%;height:100%}
  .holder{position:absolute;left:48px;top:70px}
  .holder-name{font-size:26px;font-weight:500;line-height:1.1}
  .holder-title{font-size:14px;font-weight:400;margin-top:2px}
  .front-mark{position:absolute;left:48px;top:150px;width:100px;display:flex;flex-direction:column;align-items:center;gap:8px}
  .mark-dot{width:70px;height:70px;border-radius:50%;background:var(--white)}
  .front-mark .mark-name{font-size:10px;font-weight:500;text-align:center;line-height:1.25;color:var(--white)}
  .divider{position:absolute;left:170px;top:140px;width:2px;height:180px;background:var(--white)}
  .contacts{position:absolute;left:190px;top:160px;list-style:none;font-size:14px;font-weight:500}
  .contacts li{display:flex;align-items:center;gap:10px;height:26px}
  .contacts svg{width:14px;height:14px;fill:var(--white);flex:none}
  .brand{position:absolute;left:60px;top:80px;display:flex;align-items:center;gap:16px}
  .brand .mark-dot{width:84px;height:84px;background:var(--green)}
  .brand-name{font-size:22px;font-weight:500;color:var(--gray);line-height:1.15;text-transform:uppercase;letter-spacing:.5px}
  .tagline{position:absolute;left:150px;top:230px;font-size:17px;font-weight:500;color:var(--gray)}
</style>
</head>
<body>

<section class="card card-front">
  <svg class="wedges" viewBox="0 0 600 360" aria-hidden="true">
    <polygon points="460,0 530,0 555,125" fill="var(--white)"/>
    <polygon points="600,150 600,205 420,150" fill="var(--white)"/>
    <polygon points="410,190 510,360 450,360" fill="var(--white)"/>
  </svg>
  <div class="holder">
    <p class="holder-name">Marcus Hale</p>
    <p class="holder-title">General Manager</p>
  </div>
  <div class="front-mark">
    <span class="mark-dot"></span>
    <span class="mark-name">Brightwall Sound Living Residences</span>
  </div>
  <span class="divider"></span>
  <ul class="contacts">
    <li><svg viewBox="0 0 24 24"><path d="M6.6 10.8a15.1 15.1 0 0 0 6.6 6.6l2.2-2.2a1 1 0 0 1 1-.25 11.4 11.4 0 0 0 3.6.57 1 1 0 0 1 1 1V20a1 1 0 0 1-1 1A17 17 0 0 1 3 4a1 1 0 0 1 1-1h3.5a1 1 0 0 1 1 1c0 1.25.2 2.45.57 3.6a1 1 0 0 1-.25 1z"/></svg>5550-182-437 / 5550-649-205</li>
    <li><svg viewBox="0 0 24 24"><path d="M2 5h20v14H2zm2 2v.5l8 5 8-5V7l-8 5z"/></svg>m.hale@brightwallmail.com</li>
    <li><svg viewBox="0 0 24 24"><circle cx="12" cy="12" r="10"/></svg>www.brightwallhomes.com</li>
    <li><svg viewBox="0 0 24 24"><path d="M12 2a7 7 0 0 0-7 7c0 5 7 13 7 13s7-8 7-13a7 7 0 0 0-7-7zm0 9.5A2.5 2.5 0 1 1 12 6.5a2.5 2.5 0 0 1 0 5z"/></svg>Ostler Avenue , Milbrook 4418</li>
  </ul>
</section>

<section class="card card-back">
  <svg class="wedges" viewBox="0 0 600 360" aria-hidden="true">
    <polygon points="460,0 530,0 555,125" fill="var(--green)"/>
    <polygon points="600,150 600,205 420,150" fill="var(--green)"/>
    <polygon points="410,190 510,360 450,360" fill="var(--green)"/>
  </svg>
  <div class="brand">
    <span class="mark-dot"></span>
    <p class="brand-name">Brightwall Sound<br>Living Residences</p>
  </div>
  <p class="tagline">building one dream at a Time</p>
</section>

</body>
</html>
```